Adult Residential Care Provider (Assisted Living) needs a brochure design.

We need a brochure designed for our assisted living facilites in Metairie (adjacent to New Orleans) called Willowmere Senior Homes. We provide adults, typically Seniors, a place to live where they receive 24-hour care/support of their daily living activities, including laundering, cooking, cleaning, grooming, bathing, etc.. I'd like to use our logo and the color choices should be soft and convey comfort. I would also like the brochure to be editable by my administration to make any changes in the future.

```html
<!DOCTYPE html>
<html lang="en">
<head>
<meta charset="UTF-8">
<title>Willowmere Senior Homes – Assisted Living Flyer</title>
<link href="https://fonts.googleapis.com/css2?family=Poppins:wght@400;500;600&family=Montserrat:wght@300;400;500&family=Oswald:wght@500&display=swap" rel="stylesheet">
<style>
  :root{
    --backdrop:#e0e0e0;
    --cream:#efe6d6;
    --cream-light:#f5efe3;
    --teal-deep:#164a42;
    --teal:#1f5e55;
    --teal-mid:#2a7468;
    --teal-bright:#15806f;
    --teal-text:#1b4f47;
    --white:#ffffff;
  }
  html,body{margin:0;padding:0;width:1200px;height:1200px;overflow:hidden;background:var(--backdrop);}
  .canvas{position:relative;width:1200px;height:1200px;overflow:hidden;background:var(--backdrop);}
  .flyer{
    position:absolute;left:190px;top:19px;width:1112px;height:1575px;
    transform:scale(0.7375);transform-origin:0 0;
    background:var(--cream);overflow:hidden;
    font-family:"Poppins",sans-serif;color:var(--teal-text);
  }
  .flyer h1,.flyer p,.flyer ul{margin:0;}
  .flyer-art{position:absolute;inset:0;width:1112px;height:1575px;}

  .brand{position:absolute;left:500px;top:40px;display:flex;align-items:center;gap:22px;}
  .brand-dot{width:96px;height:96px;border-radius:50%;border:4px solid var(--teal-text);box-sizing:border-box;}
  .brand-name{font-family:"Poppins",sans-serif;font-weight:600;color:var(--teal-text);line-height:1;}
  .brand-name .line-main{display:block;font-size:62px;letter-spacing:4px;}
  .brand-name .line-sub{display:block;font-size:33px;letter-spacing:3.5px;margin-top:8px;}

  .headline{position:absolute;right:32px;top:184px;text-align:right;color:var(--teal-text);font-size:inherit;}
  .headline .light{display:block;font-family:"Montserrat",sans-serif;font-weight:300;font-size:54px;line-height:60px;}
  .headline .strong{display:block;font-family:"Poppins",sans-serif;font-weight:600;font-size:54px;line-height:62px;border-bottom:3px solid var(--teal-text);padding-bottom:2px;margin-left:auto;width:max-content;}

  .provide-tab{
    position:absolute;left:405px;top:783px;width:290px;height:73px;
    background:linear-gradient(90deg,#d8ccb6,#f3ecdf 60%,#e6dccb);
    clip-path:polygon(4% 12%,8% 0,100% 0,100% 62%,96% 100%,0 100%,0 35%);
    display:flex;align-items:center;justify-content:center;
    font-family:"Poppins",sans-serif;font-weight:600;font-size:44px;color:var(--teal-text);
  }
  .provide-text{
    position:absolute;left:205px;width:700px;top:862px;text-align:center;
    font-family:"Montserrat",sans-serif;font-weight:400;font-size:29px;line-height:38px;color:#f1ebe0;
  }
  .provide-rule{position:absolute;left:360px;top:953px;width:392px;height:2px;background:#d9d1c2;}

  .services-pill{
    position:absolute;left:432px;top:1149px;width:248px;height:72px;border-radius:36px;
    background:var(--teal);color:var(--white);display:flex;align-items:center;justify-content:center;
    font-family:"Montserrat",sans-serif;font-weight:500;font-size:34px;letter-spacing:3px;
  }
  .service-list{position:absolute;top:1238px;padding:0;list-style:none;
    font-family:"Poppins",sans-serif;font-weight:500;font-size:28px;line-height:34px;color:var(--teal-text);}
  .service-list.left{left:122px;width:400px;}
  .service-list.right{left:538px;width:540px;}
  .service-list li{position:relative;padding-left:43px;}
  .tick{position:absolute;left:0;top:5px;width:28px;height:28px;}

  .phone-bar{position:absolute;left:0;top:1466px;width:495px;height:109px;
    background:linear-gradient(90deg,var(--teal-deep),var(--teal-bright));
    clip-path:polygon(0 0,100% 0,95% 100%,0 100%);}
  .phone-icon{position:absolute;left:33px;top:1485px;width:70px;height:70px;}
  .phone-number{position:absolute;left:130px;top:1484px;font-family:"Oswald",sans-serif;font-weight:500;font-size:48px;line-height:72px;color:#f1e9da;}

  .address-panel{position:absolute;left:475px;top:1428px;width:637px;height:147px;background:#17463f;
    clip-path:polygon(30px 0,100% 0,100% 100%,0 100%,24px 18px);border-top-left-radius:30px;}
  .address{position:absolute;left:518px;display:flex;align-items:center;gap:12px;
    font-family:"Montserrat",sans-serif;font-weight:500;font-size:24px;color:var(--white);}
  .address.first{top:1458px;}
  .address.second{top:1505px;}
  .address svg{width:30px;height:36px;flex:none;}
</style>
</head>
<body>
<div class="canvas">
  <div class="flyer">
    <svg class="flyer-art" viewBox="0 0 1112 1575" xmlns="http://www.w3.org/2000/svg">
      <defs>
        <linearGradient id="photoTone" x1="0" y1="0" x2="1" y2="1">
          <stop offset="0" stop-color="#d9d3c8"/>
          <stop offset="0.35" stop-color="#c8a88a"/>
          <stop offset="0.7" stop-color="#8a6b4c"/>
          <stop offset="1" stop-color="#5f5a44"/>
        </linearGradient>
        <radialGradient id="handsTone" cx="0.45" cy="0.45" r="0.7">
          <stop offset="0" stop-color="#d99a66"/>
          <stop offset="0.6" stop-color="#a8643a"/>
          <stop offset="1" stop-color="#7a4527"/>
        </radialGradient>
        <linearGradient id="tealSection" x1="0" y1="0" x2="1" y2="1">
          <stop offset="0" stop-color="#1d5a51"/>
          <stop offset="0.6" stop-color="#2b6f65"/>
          <stop offset="1" stop-color="#1f5d54"/>
        </linearGradient>
        <radialGradient id="iconDisc" cx="0.4" cy="0.35" r="0.7">
          <stop offset="0" stop-color="#2a7a6d"/>
          <stop offset="1" stop-color="#17514a"/>
        </radialGradient>
        <radialGradient id="iconShadow" cx="0.5" cy="0.5" r="0.5">
          <stop offset="0" stop-color="#000" stop-opacity="0.18"/>
          <stop offset="1" stop-color="#000" stop-opacity="0"/>
        </radialGradient>
      </defs>

      <!-- top swoosh bands -->
      <path d="M0,0 H110 C380,60 560,220 650,385 L628,395 C490,185 255,62 0,30 Z" fill="var(--teal)"/>
      <path d="M0,30 C255,62 490,185 628,395 L606,405 C465,222 245,92 0,72 Z" fill="#ffffff"/>

      <!-- main photograph area -->
      <path role="img" aria-label="Photo: a smiling elderly woman in a cream cardigan and pearls holding hands with a caregiver outdoors"
            d="M0,72 C245,92 465,222 606,405 L600,680 Q300,760 0,690 Z" fill="url(#photoTone)"/>

      <!-- teal lower section -->
      <path d="M0,700 Q300,772 600,682 L690,470 Q900,405 1112,420 V905 Q700,1115 0,962 Z" fill="url(#tealSection)"/>
      <path d="M0,690 Q300,762 600,672" fill="none" stroke="#ffffff" stroke-width="12"/>
      <path d="M1112,412 Q900,398 690,462" fill="none" stroke="#ffffff" stroke-width="10"/>
      <path d="M0,975 Q700,1128 1112,918" fill="none" stroke="#ffffff" stroke-width="10"/>

      <!-- hands photo circle -->
      <circle cx="740" cy="526" r="178" fill="var(--teal)"/>
      <circle cx="740" cy="526" r="171" fill="#ffffff"/>
      <circle cx="740" cy="526" r="164" fill="url(#handsTone)" role="img" aria-label="Photo: close-up of two clasped hands"/>

      <!-- icon discs -->
      <g class="icon-discs">
        <ellipse cx="120" cy="1100" rx="80" ry="12" fill="url(#iconShadow)"/>
        <ellipse cx="315" cy="1143" rx="62" ry="10" fill="url(#iconShadow)"/>
        <ellipse cx="492" cy="1147" rx="55" ry="9" fill="url(#iconShadow)"/>
        <ellipse cx="657" cy="1130" rx="48" ry="8" fill="url(#iconShadow)"/>
        <ellipse cx="812" cy="1100" rx="48" ry="8" fill="url(#iconShadow)"/>

        <circle cx="120" cy="1004" r="91" fill="var(--cream-light)"/>
        <circle cx="120" cy="1004" r="83" fill="url(#iconDisc)"/>
        <circle cx="315" cy="1061" r="72" fill="var(--cream-light)"/>
        <circle cx="315" cy="1061" r="65" fill="url(#iconDisc)"/>
        <circle cx="492" cy="1074" r="62" fill="var(--cream-light)"/>
        <circle cx="492" cy="1074" r="56" fill="url(#iconDisc)"/>
        <circle cx="657" cy="1066" r="54" fill="var(--cream-light)"/>
        <circle cx="657" cy="1066" r="48" fill="url(#iconDisc)"/>
        <circle cx="812" cy="1038" r="54" fill="var(--cream-light)"/>
        <circle cx="812" cy="1038" r="48" fill="url(#iconDisc)"/>
      </g>

      <!-- care icon: heart over open hands -->
      <g fill="none" stroke="#f3ede2" stroke-width="5" stroke-linecap="round" stroke-linejoin="round">
        <path d="M120,998 C100,982 82,970 82,954 C82,940 94,932 106,934 C113,935 118,940 120,945 C122,940 127,935 134,934 C146,932 158,940 158,954 C158,970 140,982 120,998 Z" fill="#f3ede2"/>
        <path d="M84,958 H100 L108,946 L116,968 L124,952 H156" stroke="#1d5a51" stroke-width="4"/>
        <path d="M72,985 L78,1010 L104,1032 V1046 M168,985 L162,1010 L136,1032 V1046"/>
        <path d="M88,1012 L106,1026 M152,1012 L134,1026"/>
        <rect x="98" y="1046" width="14" height="8"/><rect x="128" y="1046" width="14" height="8"/>
      </g>
      <!-- bathing icon: shower head -->
      <g fill="none" stroke="#f3ede2" stroke-width="5" stroke-linecap="round" stroke-linejoin="round">
        <path d="M292,1084 V1052 C292,1038 304,1032 314,1036"/>
        <path d="M306,1040 L326,1030 L338,1052 L318,1062 Z" fill="#f3ede2"/>
        <path d="M334,1062 L340,1068 M344,1056 L350,1062 M328,1070 L334,1076 M346,1046 L352,1052"/>
      </g>
      <!-- meals icon: steaming bowl -->
      <g fill="none" stroke="#f3ede2" stroke-width="4.5" stroke-linecap="round" stroke-linejoin="round">
        <path d="M462,1072 H522 C522,1090 508,1100 492,1100 C476,1100 462,1090 462,1072 Z"/>
        <path d="M480,1102 H504"/>
        <path d="M466,1054 L484,1070"/>
        <path d="M486,1060 C482,1054 490,1050 486,1044 M496,1060 C492,1054 500,1050 496,1044 M506,1060 C502,1054 510,1050 506,1044"/>
      </g>
      <!-- laundry icon: washer with shirt -->
      <g fill="none" stroke="#f3ede2" stroke-width="4" stroke-linecap="round" stroke-linejoin="round">
        <rect x="632" y="1042" width="38" height="48" rx="3"/>
        <path d="M632,1054 H670"/>
        <circle cx="651" cy="1074" r="11"/>
        <path d="M662,1066 L672,1060 H684 L692,1066 L688,1074 H684 V1090 H668"/>
      </g>
      <!-- grooming icon: comb and scissors -->
      <g fill="none" stroke="#f3ede2" stroke-width="4" stroke-linecap="round" stroke-linejoin="round">
        <path d="M786,1030 L812,1010 L820,1020 L794,1040 Z"/>
        <path d="M790,1026 L786,1020 M796,1022 L792,1016 M802,1018 L798,1012"/>
        <path d="M808,1020 L826,1052 M826,1020 L808,1052"/>
        <circle cx="830" cy="1058" r="7"/><circle cx="838" cy="1044" r="7"/>
      </g>
    </svg>

    <div class="brand">
      <div class="brand-dot"></div>
      <div class="brand-name"><span class="line-main">WILLOWMERE</span><span class="line-sub">SENIOR HOMES</span></div>
    </div>

    <h1 class="headline">
      <span class="light">Assisted Living &amp;</span>
      <span class="strong">Residential Care</span>
    </h1>

    <div class="provide-tab">We Provide</div>
    <p class="provide-text">The Love and Care Needed To Keep Your<br>Loved Ones Safely Independent.</p>
    <div class="provide-rule"></div>

    <div class="services-pill">SERVICES</div>

    <ul class="service-list left">
      <li><svg class="tick" viewBox="0 0 28 28"><circle cx="14" cy="14" r="14" fill="#1f5e55"/><path d="M8,14 L12.5,18.5 L20,10" fill="none" stroke="#fff" stroke-width="3" stroke-linecap="round" stroke-linejoin="round"/></svg>24 Hours Care</li>
      <li><svg class="tick" viewBox="0 0 28 28"><circle cx="14" cy="14" r="14" fill="#1f5e55"/><path d="M8,14 L12.5,18.5 L20,10" fill="none" stroke="#fff" stroke-width="3" stroke-linecap="round" stroke-linejoin="round"/></svg>Assistance with Daily Living Activities</li>
      <li><svg class="tick" viewBox="0 0 28 28"><circle cx="14" cy="14" r="14" fill="#1f5e55"/><path d="M8,14 L12.5,18.5 L20,10" fill="none" stroke="#fff" stroke-width="3" stroke-linecap="round" stroke-linejoin="round"/></svg>Bathing Assistance</li>
      <li><svg class="tick" viewBox="0 0 28 28"><circle cx="14" cy="14" r="14" fill="#1f5e55"/><path d="M8,14 L12.5,18.5 L20,10" fill="none" stroke="#fff" stroke-width="3" stroke-linecap="round" stroke-linejoin="round"/></svg>Beauty and Haircare</li>
      <li><svg class="tick" viewBox="0 0 28 28"><circle cx="14" cy="14" r="14" fill="#1f5e55"/><path d="M8,14 L12.5,18.5 L20,10" fill="none" stroke="#fff" stroke-width="3" stroke-linecap="round" stroke-linejoin="round"/></svg>Laundry</li>
    </ul>
    <ul class="service-list right">
      <li><svg class="tick" viewBox="0 0 28 28"><circle cx="14" cy="14" r="14" fill="#1f5e55"/><path d="M8,14 L12.5,18.5 L20,10" fill="none" stroke="#fff" stroke-width="3" stroke-linecap="round" stroke-linejoin="round"/></svg>Housekeeping</li>
      <li><svg class="tick" viewBox="0 0 28 28"><circle cx="14" cy="14" r="14" fill="#1f5e55"/><path d="M8,14 L12.5,18.5 L20,10" fill="none" stroke="#fff" stroke-width="3" stroke-linecap="round" stroke-linejoin="round"/></svg>3 Home-Cooked Meals and<br>Snacks - Dietitian Approved</li>
      <li><svg class="tick" viewBox="0 0 28 28"><circle cx="14" cy="14" r="14" fill="#1f5e55"/><path d="M8,14 L12.5,18.5 L20,10" fill="none" stroke="#fff" stroke-width="3" stroke-linecap="round" stroke-linejoin="round"/></svg>Medication Reminders and<br>Supervision</li>
    </ul>

    <div class="phone-bar"></div>
    <svg class="phone-icon" viewBox="0 0 70 70">
      <circle cx="35" cy="35" r="32" fill="none" stroke="#f1e9da" stroke-width="4"/>
      <circle cx="35" cy="35" r="24" fill="#f1e9da"/>
      <path d="M27,24 C25,26 25,30 28,35 C31,40 35,44 40,46 C43,47 46,46 47,44 L43,40 L40,42 C37,41 33,37 31,33 L33,30 L29,25 Z" fill="#1b5a51"/>
    </svg>
    <div class="phone-number">(504) 555-0184</div>

    <div class="address-panel"></div>
    <div class="address first">
      <svg viewBox="0 0 30 36"><circle cx="15" cy="18" r="14" fill="none" stroke="#d9e4e1" stroke-width="1.8"/><path d="M15,26 C11,21 9,18 9,15 A6,6 0 0 1 21,15 C21,18 19,21 15,26 Z" fill="none" stroke="#fff" stroke-width="2"/><circle cx="15" cy="15" r="2.2" fill="#fff"/></svg>
      <span>412 Larkspur Ave. Metairie, LA 70005</span>
    </div>
    <div class="address second">
      <svg viewBox="0 0 30 36"><circle cx="15" cy="18" r="14" fill="none" stroke="#d9e4e1" stroke-width="1.8"/><path d="M15,26 C11,21 9,18 9,15 A6,6 0 0 1 21,15 C21,18 19,21 15,26 Z" fill="none" stroke="#fff" stroke-width="2"/><circle cx="15" cy="15" r="2.2" fill="#fff"/></svg>
      <span>2786 Fernbrook St. Metairie, LA 70002</span>
    </div>
  </div>
</div>
</body>
</html>
```